Blue Harbor Business Cards

Name Tomas Welbridge
Title Mortgage Originator
Phone (800) 614-2290 x32
Direct (571) 362-0471
Email twelbridge@blueharborhomeloans.com
NMLS #1847362
Name Lena Ortiz
Title Mortgage Originator
Location (800) 614-2290 x55
Direct (440) 276-5190
Email lortiz@blueharborhomeloans.com
NMLS #2739418
Name Desmond Holloway-Finch
Title Mortgage Originator
Location (800) 614-2290 x56
Direct (202) 634-1975
Email dhollowayfinch@blueharborhomeloans.com
NMLS #2784530
Name Rosalyn Whitaker
Title Mortgage Originator
Location (800) 614-2290 x57
Direct (240) 358-6621
Email rwhitaker@blueharborhomeloans.com
NMLS #2491086
Name Gwen Holbrook
Title Mortgage Originator
Location (800) 614-2290 x58
Direct (540) 716-2384
Email gholbrook@blueharborhomeloans.com
NMLS #2438617
Name Ravi Dunmore
Title Mortgage Originator
Location (800) 614-2290 x59
Direct (240) 563-8827
Email rdunmore@blueharborhomeloans.com
NMLS #2597142
Name Ivy Marlow
Title Mortgage Originator
Location (800) 614-2290 x60
Direct (202) 479-3306
Email ivy@ivyfindshomes.com
NMLS #2718394
Contact Information for Business Card
Name Tomas Welbridge Title Mortgage Originator Phone (800) 614-2290 x32 Direct (571) 362-0471 Email twelbridge@blueharborhomeloans.com NMLS #1847362 Name Lena Ortiz Title Mortgage Originator Location (800) 614-2290 x55 Direct (440) 276-5190 Email lortiz@blueharborhomeloans.com NMLS #2739418 Name Desmond Holloway-Finch Title Mortgage Originator Location (800) 614-2290 x56 Direct (202) 634-1975 Email dhollowayfinch@blueharborhomeloans.com NMLS #2784530 Name Rosalyn Whitaker Title Mortgage Originator Location (800) 614-2290 x57 Direct (240) 358-6621 Email rwhitaker@blueharborhomeloans.com NMLS #2491086 Name Gwen Holbrook Title Mortgage Originator Location (800) 614-2290 x58 Direct (540) 716-2384 Email gholbrook@blueharborhomeloans.com NMLS #2438617 Name Ravi Dunmore Title Mortgage Originator Location (800) 614-2290 x59 Direct (240) 563-8827 Email rdunmore@blueharborhomeloans.com NMLS #2597142 Name Ivy Marlow Title Mortgage Originator Location (800) 614-2290 x60 Direct (202) 479-3306 Email ivy@ivyfindshomes.com NMLS #2718394
Look and feel
Each slider illustrates characteristics of the customer's brand and the style your logo design should communicate.

```html
<!DOCTYPE html>
<html lang="en">
<head>
<meta charset="utf-8">
<title>Blue Harbor Business Cards</title>
<link rel="stylesheet" href="https://fonts.googleapis.com/css2?family=Roboto+Condensed:wght@300;400;700&display=swap">
<style>
  :root {
    --stage: #000000;
    --card: #ffffff;
    --brand-blue: #0b5c87;
    --sky-line: #2ba3e6;
    --gold-dark: #d8992a;
    --gold-light: #fff1cf;
    --panel-rule: #c9dbe7;
    --photo-top: #0b5c87;
    --photo-bottom: #7fb37a;
    --photo-soft-top: #f4f6f4;
    --photo-soft-bottom: #b9d9a9;
  }
  * { margin: 0; padding: 0; box-sizing: border-box; }
  html, body {
    width: 1200px; height: 1200px; overflow: hidden;
    background: var(--stage);
    font-family: "Roboto Condensed", "Arial Narrow", sans-serif;
  }
  .card {
    position: absolute; left: 239px; width: 759px; height: 439px;
    background: var(--card); overflow: hidden;
  }
  .card--blue { top: 107px; }
  .card--white { top: 623px; }
  .card__portrait { position: absolute; left: 0; top: 0; width: 759px; height: 439px; }
  .brand {
    position: absolute; left: 400px; top: 56px;
    display: flex; align-items: center; gap: 10px;
    color: var(--brand-blue); font-weight: 700; font-size: 36px; letter-spacing: 0.5px;
  }
  .brand__dot { width: 26px; height: 26px; border-radius: 50%; background: var(--brand-blue); }
  .person__name {
    position: absolute; left: 372px; top: 151px;
    color: var(--brand-blue); font-weight: 700; font-size: 43px; line-height: 1;
    text-transform: uppercase; white-space: nowrap;
  }
  .person__title {
    position: absolute; left: 372px; top: 196px;
    color: var(--brand-blue); font-weight: 400; font-size: 37px; line-height: 1;
    white-space: nowrap;
  }
  .rule-sky { position: absolute; left: 373px; right: 0; top: 252px; height: 4px; background: var(--sky-line); }
  .rule-gold {
    position: absolute; left: 373px; right: 0; top: 263px; height: 9px;
    background: linear-gradient(90deg, var(--gold-dark) 0%, var(--gold-light) 22%, var(--gold-dark) 55%, #f0b441 80%, var(--gold-dark) 100%);
  }
  .contact {
    position: absolute; left: 373px; right: 0; top: 272px; bottom: 0;
    background: var(--brand-blue); color: #ffffff; font-weight: 300;
  }
  .contact__line { position: absolute; left: 19px; white-space: nowrap; line-height: 1; }
  .contact__line--phone { top: 13px; font-size: 27px; }
  .contact__line--direct { top: 47px; font-size: 27px; }
  .contact__divider { position: absolute; left: 16px; width: 331px; top: 86px; height: 1px; background: var(--panel-rule); }
  .contact__line--email { top: 98px; font-size: 20px; letter-spacing: -0.1px; }
  .contact__line--nmls { top: 128px; font-size: 26px; }
</style>
</head>
<body>

<section class="card card--blue">
  <svg class="card__portrait" viewBox="0 0 759 439" role="img" aria-label="Portrait photo of the loan originator in a green shirt and dark tie on a blue background">
    <defs>
      <linearGradient id="portraitBlue" x1="0" y1="0" x2="0" y2="1">
        <stop offset="0" stop-color="var(--photo-top)"/>
        <stop offset="0.45" stop-color="var(--photo-top)"/>
        <stop offset="1" stop-color="var(--photo-bottom)"/>
      </linearGradient>
    </defs>
    <circle cx="18" cy="118" r="321" fill="url(#portraitBlue)"/>
  </svg>
  <div class="brand"><span class="brand__dot"></span><span class="brand__name">Blue Harbor</span></div>
  <h1 class="person__name">Tomas Welbridge</h1>
  <p class="person__title">Mortgage Originator</p>
  <div class="rule-sky"></div>
  <div class="rule-gold"></div>
  <div class="contact">
    <p class="contact__line contact__line--phone">(800) 614-2290 x32</p>
    <p class="contact__line contact__line--direct">Direct (571) 362-0471</p>
    <div class="contact__divider"></div>
    <p class="contact__line contact__line--email">Email twelbridge@blueharborhomeloans.com</p>
    <p class="contact__line contact__line--nmls">NMLS #1847362</p>
  </div>
</section>

<section class="card card--white">
  <svg class="card__portrait" viewBox="0 0 759 439" role="img" aria-label="Portrait photo of the loan originator in a green shirt and dark tie on a white background">
    <defs>
      <linearGradient id="portraitSoft" x1="0" y1="0" x2="0" y2="1">
        <stop offset="0" stop-color="var(--photo-soft-top)"/>
        <stop offset="0.45" stop-color="var(--photo-soft-top)"/>
        <stop offset="1" stop-color="var(--photo-soft-bottom)"/>
      </linearGradient>
      <filter id="edgeShade" x="-10%" y="-10%" width="120%" height="120%">
        <feGaussianBlur stdDeviation="5"/>
      </filter>
    </defs>
    <circle cx="14" cy="118" r="322" fill="#d2d2d2" filter="url(#edgeShade)"/>
    <circle cx="18" cy="118" r="321" fill="url(#portraitSoft)"/>
  </svg>
  <div class="brand"><span class="brand__dot"></span><span class="brand__name">Blue Harbor</span></div>
  <h1 class="person__name">Tomas Welbridge</h1>
  <p class="person__title">Mortgage Originator</p>
  <div class="rule-sky"></div>
  <div class="rule-gold"></div>
  <div class="contact">
    <p class="contact__line contact__line--phone">(800) 614-2290 x32</p>
    <p class="contact__line contact__line--direct">Direct (571) 362-0471</p>
    <div class="contact__divider"></div>
    <p class="contact__line contact__line--email">Email twelbridge@blueharborhomeloans.com</p>
    <p class="contact__line contact__line--nmls">NMLS #1847362</p>
  </div>
</section>

</body>
</html>
```